Parkinson's Disease Progression

Visually describe the rate of Parkinson progression in the first 15 years following diagnosis. Title: "Patient-Perceived Progression of Parkinsonism"

The attached figure names "meanqol" is the curve that should serve as the basis of this graphic. Everything else-- color, labels, font, etc. describe this curve.
Thank you!

Target Market(s)

People with Parkisnon's Disease, neurologists, family members.

Font styles to use
Sans Serif

Requirements
Must have
• Must have the lines going through these exact numbers
Excellent -- 502
Very good- 661
Good- 895
Fair- 1268
Poor- 1655

LABELS:
Title: "Patient-Perceived Progression of Parkinsonism"
"SWI-TC (Self-Logged Wellbeing Index for Tremor Conditions)" should be the label on the left.
"Quality of Life" should be the label on the right
"Years Since Diagnosis" should be the label on the bottom
Nice to have
• A color scheme that goes from GOOD (low numbers) to BAD (high numbers).

Easy to read (elderly)

```html
<!DOCTYPE html>
<html lang="en">
<head>
<meta charset="utf-8">
<title>Patient-Perceived Progression of Parkinsonism</title>
<link href="https://fonts.googleapis.com/css2?family=Barlow+Condensed:wght@400;600;700;800&display=swap" rel="stylesheet">
<style>
  :root {
    --paper: #ffffff;
    --ink: #111111;
    --band-poor-above: #fbf8d4;
    --band-fair: #a6d8b8;
    --band-good: #30b7c5;
    --band-very-good: #2482bb;
    --band-excellent: #263f90;
    --divider: #ffffff;
    --tag: #ffffff;
  }
  html, body {
    margin: 0;
    padding: 0;
    width: 1200px;
    height: 848px;
    overflow: hidden;
    background: var(--paper);
  }
  .chart {
    display: block;
    width: 1200px;
    height: 848px;
    font-family: "Barlow Condensed", "Arial Narrow", sans-serif;
  }
  .chart-title {
    font-weight: 800;
    font-size: 31px;
    letter-spacing: 0.5px;
    fill: var(--ink);
  }
  .tick-label {
    font-weight: 700;
    font-size: 18px;
    fill: var(--ink);
  }
  .axis-title {
    font-weight: 400;
    font-size: 25px;
    letter-spacing: 0.6px;
    fill: var(--ink);
  }
  .band-tag rect { fill: var(--tag); }
  .band-tag text {
    font-weight: 700;
    font-size: 16px;
    fill: var(--ink);
  }
  .band-divider {
    stroke: var(--divider);
    stroke-width: 1.6;
    stroke-dasharray: 2 3;
  }
  .axis-line {
    stroke: var(--ink);
    stroke-width: 4;
    fill: none;
  }
  .tick { stroke: var(--ink); stroke-width: 2; }
  .mean-curve { stroke: var(--ink); stroke-width: 3.2; fill: none; stroke-linecap: round; }
  .ci-edge { stroke: var(--ink); stroke-width: 1.2; stroke-dasharray: 5 4; fill: none; }
</style>
</head>
<body>
<svg class="chart" viewBox="0 0 1200 848" xmlns="http://www.w3.org/2000/svg" role="img" aria-label="Line chart of patient-perceived progression of parkinsonism over 15 years since diagnosis">
  <defs>
    <linearGradient id="ci-fill" x1="0" y1="0" x2="1" y2="0">
      <stop offset="0" stop-color="#ffffff" stop-opacity="0.55"/>
      <stop offset="0.3" stop-color="#ffffff" stop-opacity="0.8"/>
      <stop offset="0.8" stop-color="#ffffff" stop-opacity="0.7"/>
      <stop offset="1" stop-color="#ffffff" stop-opacity="0"/>
    </linearGradient>
    <linearGradient id="start-haze" x1="0" y1="0" x2="1" y2="0">
      <stop offset="0" stop-color="#8a7fc9" stop-opacity="0.55"/>
      <stop offset="1" stop-color="#8a7fc9" stop-opacity="0"/>
    </linearGradient>
  </defs>

  <text class="chart-title" x="145" y="98">PATIENT-PERCEIVED PROGRESSION OF PARKINSONISM</text>

  <!-- quality-of-life bands -->
  <g class="bands">
    <rect x="268" y="141" width="699" height="144" fill="var(--band-poor-above)"/>
    <rect x="268" y="285" width="699" height="122" fill="var(--band-fair)"/>
    <rect x="268" y="407" width="699" height="76" fill="var(--band-good)"/>
    <rect x="268" y="483" width="699" height="52" fill="var(--band-very-good)"/>
    <rect x="268" y="535" width="699" height="145" fill="var(--band-excellent)"/>
    <line class="band-divider" x1="268" y1="285" x2="967" y2="285"/>
    <line class="band-divider" x1="268" y1="407" x2="967" y2="407"/>
    <line class="band-divider" x1="268" y1="483" x2="967" y2="483"/>
    <line class="band-divider" x1="268" y1="535" x2="967" y2="535"/>
  </g>

  <!-- confidence band and mean curve -->
  <g class="series">
    <path d="M268 505 L289 523 L289 591 L268 620 Z" fill="url(#start-haze)"/>
    <path fill="url(#ci-fill)" d="M289 523 C330 515 390 490 449 470 S520 450 529 452 S600 440 649 420 S740 370 809 340 S870 305 889 291 L889 389 C860 380 840 385 809 383 C760 386 690 425 649 437 C600 455 560 468 529 470 C500 472 470 473 449 478 C400 490 330 550 289 591 Z"/>
    <path class="ci-edge" d="M289 523 C330 515 390 490 449 470 S520 450 529 452 S600 440 649 420 S740 370 809 340 S870 305 889 291"/>
    <path class="ci-edge" d="M289 591 C330 550 400 490 449 478 S520 468 529 470 S600 462 649 437 S760 386 809 383 S860 380 889 389"/>
    <path class="mean-curve" d="M289 552 C320 535 360 512 389 497 S460 465 489 462 S560 458 589 451 S660 416 689 405 S760 373 809 360 S870 346 889 343"/>
  </g>

  <!-- band tags -->
  <g class="band-tag"><rect x="894" y="254" width="73" height="22"/><text x="955" y="271" text-anchor="end">POOR</text></g>
  <g class="band-tag"><rect x="894" y="377" width="73" height="22"/><text x="955" y="394" text-anchor="end">FAIR</text></g>
  <g class="band-tag"><rect x="894" y="453" width="73" height="22"/><text x="955" y="470" text-anchor="end">GOOD</text></g>
  <g class="band-tag"><rect x="850" y="506" width="117" height="22"/><text x="955" y="523" text-anchor="end">VERY GOOD</text></g>
  <g class="band-tag"><rect x="850" y="652" width="117" height="22"/><text x="955" y="669" text-anchor="end">EXCELLENT</text></g>

  <!-- axes -->
  <path class="axis-line" d="M268 141 V692 H967"/>
  <g class="y-ticks">
    <line class="tick" x1="262" y1="176" x2="268" y2="176"/>
    <line class="tick" x1="262" y1="241" x2="268" y2="241"/>
    <line class="tick" x1="262" y1="307" x2="268" y2="307"/>
    <line class="tick" x1="262" y1="372" x2="268" y2="372"/>
    <line class="tick" x1="262" y1="438" x2="268" y2="438"/>
    <line class="tick" x1="262" y1="503" x2="268" y2="503"/>
    <line class="tick" x1="262" y1="569" x2="268" y2="569"/>
    <line class="tick" x1="262" y1="634" x2="268" y2="634"/>
    <text class="tick-label" x="244" y="182" text-anchor="end">1600</text>
    <text class="tick-label" x="244" y="247" text-anchor="end">1400</text>
    <text class="tick-label" x="244" y="313" text-anchor="end">1200</text>
    <text class="tick-label" x="244" y="378" text-anchor="end">1000</text>
    <text class="tick-label" x="244" y="444" text-anchor="end">800</text>
    <text class="tick-label" x="244" y="509" text-anchor="end">600</text>
    <text class="tick-label" x="244" y="575" text-anchor="end">400</text>
    <text class="tick-label" x="244" y="640" text-anchor="end">200</text>
  </g>
  <g class="x-ticks">
    <line class="tick" x1="489" y1="692" x2="489" y2="699"/>
    <line class="tick" x1="689" y1="692" x2="689" y2="699"/>
    <line class="tick" x1="889" y1="692" x2="889" y2="699"/>
    <text class="tick-label" x="289" y="737" text-anchor="middle">0</text>
    <text class="tick-label" x="489" y="737" text-anchor="middle">5</text>
    <text class="tick-label" x="689" y="737" text-anchor="middle">10</text>
    <text class="tick-label" x="889" y="737" text-anchor="middle">15</text>
  </g>

  <!-- axis titles -->
  <text class="axis-title" x="607" y="782" text-anchor="middle">YEARS SINCE DIAGNOSIS</text>
  <text class="axis-title" transform="translate(168 424) rotate(-90)" text-anchor="middle">SELF-LOGGED WELLBEING INDEX</text>
  <text class="axis-title" transform="translate(1026 424) rotate(-90)" text-anchor="middle">QUALITY OF LIFE</text>
</svg>
</body>
</html>
```